Can you make a cool and versatile Talvern Ridge Powerpoint template?
See www.talvernridge.co.uk and http://www.linkedin.com/company/talvern-ridge-ltd/ (on the right) to see how the logos are currently used - with interchangeably white and black backgrounds.
Target Market(s)
Marketing managers, product managers in HR technology, HR consultants
Industry/Entity Type
It Company
Font styles to use
Sans Serif
Requirements
Must have
- Master slide design, fonts, color theme, etc. Ideally two variations - one with white background (using colorful logo), one with a darker background (using black/white logo).

```html
<!DOCTYPE html>
<html lang="en">
<head>
<meta charset="utf-8">
<title>Talvern Ridge – Presentation Template</title>
<link href="https://fonts.googleapis.com/css2?family=Arimo:wght@400;700&display=swap" rel="stylesheet">
<style>
:root{
  --canvas:#ffffff;
  --slide:#000000;
  --ink:#ffffff;
  --red:#e61e2a;
  --orange:#ee4c22;
  --yellow:#f7c20f;
  --lime:#a6c83a;
  --green:#2e8a4f;
  --blue:#2f3192;
  --purple:#8a2a6e;
  --magenta:#872a66;
  --pink:#f46fc6;
  --sky:#0b63c9;
  --amber:#f7962a;
  --bullet:#2e8a4f;
}
*{margin:0;padding:0;box-sizing:border-box}
html,body{width:1200px;height:1000px;overflow:hidden;background:var(--canvas)}
body{position:relative;font-family:"Arimo",Arial,sans-serif;color:var(--ink)}
.slide{position:absolute;width:560px;height:354px;background:var(--slide);overflow:hidden}
.slide--cover{left:48px;top:103px}
.slide--charts{left:615px;top:103px}
.slide--people{left:48px;top:508px}
.slide--stats{left:615px;top:508px}
.abs{position:absolute}
.header-mark{left:0;top:21px;width:35px;height:36px;background:var(--red)}
.title{left:36px;top:18px;font-size:23px;font-weight:700;letter-spacing:.2px;line-height:1}
.subtitle{left:36px;top:45px;font-size:14.5px;font-weight:700;line-height:1}
.brand{left:36px;top:326px;font-size:14px;font-weight:400}
.site{right:35px;top:326px;font-size:11px;font-weight:700}
.body-copy{font-size:10.5px;font-weight:700;line-height:13px}
.caption{font-size:8px;font-weight:700;line-height:10.5px}
/* cover */
.cover-word{left:280px;top:118px;font-size:34px;font-weight:700;letter-spacing:.5px}
.cover-title{left:48px;top:216px;font-size:23px;font-weight:700;line-height:1}
.cover-sub{left:48px;top:243px;font-size:14.5px;font-weight:700;line-height:1}
/* bullets */
.bullets{left:37px;width:500px;list-style:none}
.bullets li{position:relative;padding-left:20px;margin-bottom:13px;font-size:10.5px;font-weight:700;line-height:13px}
.bullets li::before{content:"";position:absolute;left:0;top:3px;width:9px;height:9px;border-radius:50%;background:var(--bullet)}
.people-group{top:170px;width:142px;height:58px}
.pct{font-size:37px;font-weight:700;fill:var(--ink)}
</style>
</head>
<body>

<section class="slide slide--cover">
  <div class="abs cover-word">Talvern Ridge</div>
  <div class="abs cover-title">LOREM IPSUM</div>
  <div class="abs cover-sub">Your Business Theme Here</div>
  <div class="abs site" style="top:326px">www.talvernridge.co.uk</div>
</section>

<section class="slide slide--charts">
  <div class="abs header-mark"></div>
  <div class="abs title">LOREM IPSUM</div>
  <div class="abs subtitle">Your Business Theme Here</div>
  <p class="abs body-copy" style="left:40px;top:92px;width:150px">Lorem ipsum dolor<br>sit amet, consectetur<br>adipisicing elit, sed do<br>eiusmod tempor<br>incididunt ut labore<br>et dolore magna aliqua.</p>
  <p class="abs body-copy" style="left:40px;top:185px;width:150px">Lorem ipsum dolor<br>sit amet, consectetur<br>adipisicing elit, sed do<br>eiusmod tempor<br>incididunt ut labore<br>et dolore magna aliqua.</p>

  <svg class="abs segment-wheel" style="left:181px;top:70px" width="180" height="180" viewBox="0 0 180 180">
    <g transform="rotate(-90 90 90)" fill="none" stroke-width="65">
      <circle cx="90" cy="90" r="52.5" stroke="var(--orange)" stroke-dasharray="44.1 285.77" stroke-dashoffset="-1.5"/>
      <circle cx="90" cy="90" r="52.5" stroke="var(--yellow)" stroke-dasharray="44.1 285.77" stroke-dashoffset="-48.6"/>
      <circle cx="90" cy="90" r="52.5" stroke="var(--lime)" stroke-dasharray="44.1 285.77" stroke-dashoffset="-95.7"/>
      <circle cx="90" cy="90" r="52.5" stroke="var(--green)" stroke-dasharray="44.1 285.77" stroke-dashoffset="-142.8"/>
      <circle cx="90" cy="90" r="52.5" stroke="var(--blue)" stroke-dasharray="44.1 285.77" stroke-dashoffset="-190"/>
      <circle cx="90" cy="90" r="52.5" stroke="var(--purple)" stroke-dasharray="44.1 285.77" stroke-dashoffset="-237.1"/>
      <circle cx="90" cy="90" r="52.5" stroke="var(--red)" stroke-dasharray="44.1 285.77" stroke-dashoffset="-284.2"/>
    </g>
    <g font-family="Arimo, Arial, sans-serif" font-size="10" font-weight="700" fill="#fff" text-anchor="middle">
      <text x="116" y="35"><tspan x="116">LOREM</tspan><tspan x="116" dy="10">IPSUM</tspan></text>
      <text x="142" y="76"><tspan x="142">LOREM</tspan><tspan x="142" dy="10">IPSUM</tspan></text>
      <text x="134" y="126"><tspan x="134">LOREM</tspan><tspan x="134" dy="10">IPSUM</tspan></text>
      <text x="90" y="153"><tspan x="90">LOREM</tspan><tspan x="90" dy="10">IPSUM</tspan></text>
      <text x="43" y="126"><tspan x="43">LOREM</tspan><tspan x="43" dy="10">IPSUM</tspan></text>
      <text x="32" y="76"><tspan x="32">LOREM</tspan><tspan x="32" dy="10">IPSUM</tspan></text>
      <text x="64" y="35"><tspan x="64">LOREM</tspan><tspan x="64" dy="10">IPSUM</tspan></text>
    </g>
  </svg>

  <svg class="abs pyramid" style="left:360px;top:69px" width="166" height="174" viewBox="0 0 166 174">
    <polygon points="83,0 115.4,68 50.6,68" fill="var(--blue)"/>
    <polygon points="47.7,74 118.3,74 138.3,116 27.7,116" fill="var(--purple)"/>
    <polygon points="24.8,122 141.2,122 166,174 0,174" fill="var(--red)"/>
    <g font-family="Arimo, Arial, sans-serif" font-size="9" font-weight="700" fill="#fff" text-anchor="middle">
      <text x="83" y="50"><tspan x="83">LOREM</tspan><tspan x="83" dy="9">IPSUM</tspan></text>
      <text x="83" y="99">LOREM IPSUM</text>
      <text x="83" y="151">LOREM IPSUM</text>
    </g>
  </svg>

  <p class="abs caption" style="left:217px;top:254px">Lorem ipsum dolor sit amet,<br>consectetur adipisicing elit,<br>sed do eiusmod tempor.</p>
  <p class="abs caption" style="left:388px;top:254px">Lorem ipsum dolor sit amet,<br>consectetur adipisicing elit,<br>sed do eiusmod tempor.</p>
  <div class="abs brand">Talvern Ridge</div>
  <div class="abs site">www.talvernridge.co.uk</div>
</section>

<section class="slide slide--people">
  <div class="abs header-mark"></div>
  <div class="abs title">LOREM IPSUM</div>
  <div class="abs subtitle">Your Business Theme Here</div>
  <ul class="abs bullets" style="top:77px">
    <li>Lorem ipsum dolor sit amet, consectetur adipisicing elit,<br>sed do eiusmod tempor incididunt ut labore et dolore magna aliqua.</li>
    <li>Lorem ipsum dolor sit amet, consectetur adipisicing elit,<br>sed do eiusmod tempor incididunt ut labore et dolore magna aliqua.</li>
  </ul>
  <div class="abs people-group" style="left:39px;background:var(--blue)" role="img" aria-label="Three blue person icons representing a team group"></div>
  <div class="abs people-group" style="left:212px;background:var(--orange)" role="img" aria-label="Three orange person icons representing a team group"></div>
  <div class="abs people-group" style="left:384px;background:var(--green)" role="img" aria-label="Three green person icons representing a team group"></div>
  <p class="abs caption" style="left:40px;top:244px">Lorem ipsum dolor sit amet,<br>consectetur adipisicing elit,<br>sed do eiusmod tempor.</p>
  <p class="abs caption" style="left:213px;top:244px">Lorem ipsum dolor sit amet,<br>consectetur adipisicing elit,<br>sed do eiusmod tempor.</p>
  <p class="abs caption" style="left:385px;top:244px">Lorem ipsum dolor sit amet,<br>consectetur adipisicing elit,<br>sed do eiusmod tempor.</p>
  <div class="abs brand">Talvern Ridge</div>
  <div class="abs site">www.talvernridge.co.uk</div>
</section>

<section class="slide slide--stats">
  <div class="abs header-mark"></div>
  <div class="abs title">LOREM IPSUM</div>
  <div class="abs subtitle">Your Business Theme Here</div>
  <ul class="abs bullets" style="top:77px">
    <li>Lorem ipsum dolor sit amet, consectetur adipisicing elit,<br>sed do eiusmod tempor incididunt ut labore et dolore magna aliqua.ua.</li>
  </ul>

  <svg class="abs stat-pie" style="left:37px;top:120px" width="120" height="120" viewBox="0 0 120 120">
    <circle cx="60" cy="60" r="60" fill="var(--magenta)"/>
    <path d="M60,60 L60,0 A60,60 0 0,0 30,8.04 Z" fill="var(--pink)"/>
    <text class="pct" x="60" y="73" text-anchor="middle" font-family="Arimo, Arial, sans-serif">96%</text>
  </svg>
  <svg class="abs stat-pie" style="left:223px;top:120px" width="120" height="120" viewBox="0 0 120 120">
    <circle cx="60" cy="60" r="60" fill="var(--blue)"/>
    <path d="M60,60 L60,0 A60,60 0 0,0 2.04,75.5 Z" fill="var(--sky)"/>
    <text class="pct" x="60" y="73" text-anchor="middle" font-family="Arimo, Arial, sans-serif">86%</text>
  </svg>
  <svg class="abs stat-pie" style="left:400px;top:120px" width="120" height="120" viewBox="0 0 120 120">
    <circle cx="60" cy="60" r="60" fill="var(--orange)"/>
    <path d="M60,60 L60,0 A60,60 0 0,0 2.04,75.5 Z" fill="var(--amber)"/>
    <text class="pct" x="60" y="73" text-anchor="middle" font-family="Arimo, Arial, sans-serif">88%</text>
  </svg>

  <p class="abs caption" style="left:38px;top:246px">Lorem ipsum dolor sit amet,<br>consectetur adipisicing elit,<br>sed do eiusmod tempor.</p>
  <p class="abs caption" style="left:232px;top:246px">Lorem ipsum dolor sit amet,<br>consectetur adipisicing elit,<br>sed do eiusmod tempor.</p>
  <p class="abs caption" style="left:398px;top:246px">Lorem ipsum dolor sit amet,<br>consectetur adipisicing elit,<br>sed do eiusmod tempor.</p>
  <div class="abs brand">Talvern Ridge</div>
  <div class="abs site">www.talvernridge.co.uk</div>
</section>

</body>
</html>
```